Stylist/Barber Standup Sign for Hair Regrowth Company

We want to design an attractive and eye-catching sign for hair stylists and barbers to sit on their workstations to attract the attention of their clients regarding hair loss and encourage them to speak to their stylist about it of they are would like to seek treatment.
50% of men and 25% of women suffer from hair loss but most are in denial that it is happening or too embarrassed to talk about it.

Copy for the flyer is as follows:

[Section 1:]
This flyer has been placed here/designed to spark conversation about hair loss

[Section 2:]
The truth is...
73% of people believe their hair is thinning
They are right

[Section 3:]
If you've got questions, your stylist or barber has answers.

Additional Background Information:

Primary target audience is men between the ages of 25-45, secondary target audience is men 46-60

Current Consumer Perception? (in the first person) “I’ve been thinking about my hair. I think it’s getting thinner and I’m scared, worried and don’t know what to do. But I don’t know if there is anything that really works. I’ve tried other things and nothing‘s worked.”

Tonality of materials? Very guy friendly, matter of fact, authoritative, its what you might hear from your best friend. Confident. Encouraging, but with a sense of urgency.

Please use our brand colors, but do not include our logo or brand name.
Colors are as follows:
Green: #4ca26f
Light Grey: #999999
Dark Grey: #262626

I have attached print templates in both PDF and Jpeg, please use those to provide final ready to print documents if you are selected.

Target Market(s)

Industry/Entity Type

Health And Wellness

Font styles to use
Sans Serif

Colors
00a990
ffffff
333333
cbcbcb

Requirements
Must have
• We want to get across the following messaging. Ideally you will submit a design using our copy and if you think you can do better, please feel free to submit another design with your own copy/messaging. If you can do it better we would love to select you :-)
• Our copy?
• This flyer has been placed here/designed to spark conversation about hair loss
• The truth is...
• 73% of people believe their hair is thinning
• They are right
• If you've got questions, your stylist or barber has answers
• Also please use our brand colors:
• Green: #4ca26f
• Light Grey: #999999
• Dark Grey: #262626
Should not have
• dont add any logos, images or ornate design. this needs to be simple, easy to ready and eye catching.
• do not use the color red in any capacity.

```html
<!DOCTYPE html>
<html lang="en">
<head>
<meta charset="utf-8">
<title>Hair Loss Conversation Standup Sign</title>
<link rel="stylesheet" href="https://fonts.googleapis.com/css2?family=Raleway:wght@400;500;800&family=Nunito+Sans:wght@400;600&display=swap">
<style>
  :root {
    --teal: #1aa58f;
    --ink: #333333;
    --paper: #ffffff;
    --backdrop: #737477;
  }
  * { margin: 0; padding: 0; box-sizing: border-box; }
  html, body {
    width: 1200px;
    height: 1000px;
    overflow: hidden;
    background: var(--backdrop);
  }
  .sign {
    position: absolute;
    left: 310px;
    top: 68px;
    width: 580px;
    height: 864px;
    background: var(--paper);
    color: var(--ink);
  }
  .frame-outer {
    position: absolute;
    left: 19px; top: 19px;
    width: 541px; height: 825px;
    border: 2px solid var(--teal);
  }
  .frame-inner {
    position: absolute;
    left: 24px; top: 24px;
    width: 531px; height: 815px;
    border: 1px solid var(--teal);
  }
  .line {
    position: absolute;
    left: 0; right: 0;
    text-align: center;
    white-space: nowrap;
  }
  .body-text {
    font-family: "Nunito Sans", sans-serif;
    font-size: 21px;
    line-height: 30px;
    height: 30px;
  }
  .label {
    font-family: "Raleway", sans-serif;
    font-weight: 500;
    font-size: 22px;
    line-height: 30px;
    height: 30px;
    color: var(--teal);
  }
  .statement {
    font-family: "Raleway", sans-serif;
    font-weight: 500;
    font-size: 32px;
    line-height: 44px;
    height: 44px;
  }
  .accent { color: var(--teal); }
  .caps { letter-spacing: 0.2px; }
  .bar {
    position: absolute;
    height: 4px;
    width: 73px;
    background: var(--teal);
  }
  .rule {
    position: absolute;
    height: 2px;
    width: 387px;
    background: var(--teal);
  }
  .quote-mark {
    position: absolute;
    font-family: "Raleway", sans-serif;
    font-weight: 800;
    font-size: 54px;
    line-height: 1;
    color: var(--teal);
  }
</style>
</head>
<body>
  <main class="sign">
    <div class="frame-outer"></div>
    <div class="frame-inner"></div>

    <section class="intro">
      <p class="line body-text" style="top:61px;">This flyer has been placed here/ designed</p>
      <p class="line body-text" style="top:90px;">to spark conversation about</p>
      <p class="line label" style="top:126px;">HAIR LOSS</p>
      <div class="bar" style="left:253px; top:160px;"></div>
    </section>

    <section class="truth">
      <span class="quote-mark" style="left:84px; top:263px;">&ldquo;</span>
      <div class="rule" style="left:118px; top:292px;"></div>
      <blockquote>
        <p class="line statement" style="top:322px;">The Truth is...</p>
        <p class="line statement" style="top:367px;">73% of People Believe</p>
        <p class="line statement accent" style="top:411px;">Their Hair is Thinning</p>
      </blockquote>
      <div class="rule" style="left:86px; top:489px;"></div>
      <span class="quote-mark" style="left:482px; top:483px;">&rdquo;</span>
      <p class="line body-text" style="top:513px;">and</p>
      <p class="line body-text caps" style="top:551px;">THEY ARE RIGHT</p>
    </section>

    <section class="answers">
      <p class="line body-text" style="top:690px;">If you've got questions,</p>
      <p class="line label" style="top:725px;">YOUR STYLIST OR BARBER</p>
      <p class="line label" style="top:760px;">HAS ANSWERS.</p>
      <div class="bar" style="left:282px; top:793px;"></div>
    </section>
  </main>
</body>
</html>
```